Linked In Business banner needed

The image size is 1128 px X 191 px

This is a LinkedIn Company Banner. Mora Pell Kite is the company and I have attached our logo. We are an advance staffing company that only recruits sales professionals.

```html
<!DOCTYPE html>
<html lang="en">
<head>
<meta charset="UTF-8">
<title>Mora Pell Kite – Company Banner</title>
<link href="https://fonts.googleapis.com/css2?family=Poppins:wght@300;400;600;800&display=swap" rel="stylesheet">
<style>
  :root {
    --navy-deep: #060b1c;
    --navy-mid: #0d1834;
    --photo-blue-dark: #1d3f86;
    --photo-blue: #3461b4;
    --photo-blue-light: #5a85cf;
    --accent-cyan: #1f9ff0;
    --white: #ffffff;
    --muted: #c8d3e8;
  }
  * { margin: 0; padding: 0; box-sizing: border-box; }
  html, body {
    width: 1200px;
    height: 203px;
    overflow: hidden;
    background: var(--navy-deep);
  }
  .banner {
    position: relative;
    width: 1200px;
    height: 203px;
    overflow: hidden;
    font-family: "Poppins", sans-serif;
  }
  .brand-panel {
    position: absolute;
    inset: 0;
    background: radial-gradient(ellipse at 20% 40%, #16264a 0%, var(--navy-mid) 40%, var(--navy-deep) 100%);
  }
  .team-photo {
    position: absolute;
    inset: 0;
    clip-path: polygon(468px 0, 1200px 0, 1200px 203px, 425px 203px);
    background: linear-gradient(100deg, var(--photo-blue-dark) 0%, var(--photo-blue) 45%, var(--photo-blue-light) 75%, var(--photo-blue) 100%);
  }
  .divider {
    position: absolute;
    inset: 0;
  }
  .brand {
    position: absolute;
    left: 85px;
    top: 86px;
    display: flex;
    flex-direction: column;
    align-items: flex-start;
  }
  .brand-name {
    display: flex;
    align-items: center;
    gap: 10px;
    color: var(--white);
    font-weight: 600;
    font-size: 29px;
    line-height: 1;
    letter-spacing: 0.5px;
  }
  .brand-mark {
    width: 14px;
    height: 14px;
    background: var(--accent-cyan);
  }
  .brand-tagline {
    margin-top: 9px;
    padding-top: 4px;
    border-top: 1.5px solid var(--muted);
    width: 266px;
    text-align: right;
    color: var(--white);
    font-weight: 600;
    font-size: 9px;
    letter-spacing: 0.6px;
  }
  .headline {
    position: absolute;
    left: 502px;
    top: 80px;
    color: var(--white);
  }
  .headline-intro {
    font-weight: 300;
    font-size: 28px;
    line-height: 1.1;
  }
  .headline-focus {
    margin-top: 4px;
    font-weight: 800;
    font-size: 26.5px;
    line-height: 1.1;
    text-transform: uppercase;
  }
</style>
</head>
<body>
  <div class="banner">
    <div class="brand-panel" role="img" aria-label="Dark navy background with soft flowing wave lines"></div>
    <div class="team-photo" role="img" aria-label="Photo of two smiling sales professionals with a blue colour overlay"></div>
    <svg class="divider" width="1200" height="203" viewBox="0 0 1200 203" aria-hidden="true">
      <polygon points="462,0 474,0 431,203 419,203" fill="var(--accent-cyan)"/>
    </svg>

    <div class="brand">
      <div class="brand-name"><span>Mora Pell Kite</span><span class="brand-mark"></span></div>
      <div class="brand-tagline">YOUR A.I. SALES RECRUITER</div>
    </div>

    <div class="headline">
      <p class="headline-intro">Advance staffing company that</p>
      <p class="headline-focus">Only recruits sales professionals</p>
    </div>
  </div>
</body>
</html>
```